Clear Plastic Card Design

I am looking to have a business card designed from my logo icon. I am looking to match the style of a different business card I have attached in the files.
Looking for a card that is plastic, with layers of transparency in the shape of my logo icon (also attached in the files) - not a circle like the other card. The winning design will incorporate the red icon logo on the front and back and include the charity's name, "Lanterns of Willow Creek" in the same or similar font, as well as an email and phone number. For now, use the email: email@lanternsofwillowcreek.org and the phone number 555-014-7392.
We like how the sample business card has transparency, partial and full opacity layers and a matching color scheme. Files will need to be in vector so that our business card printing company can work with it.
UPDATE:
We've some excellent designs in, thank you everyone! I got an early review from the owner, and he requested a minor redirect to find his perfect design. He wants the design to stand out by NOT being a rectangle. Try instead a circle, square, or best yet - something that falls in the outline of the logo icon, either fully or partially. Thank you, everyone!
Lanterns of Willow Creek text should be incorporated as well as a phone and email.

```html
<!DOCTYPE html>
<html lang="en">
<head>
<meta charset="utf-8">
<title>Lanterns of Willow Creek – Clear Business Card</title>
<link rel="stylesheet" href="https://fonts.googleapis.com/css2?family=Poppins:wght@400;600&display=swap">
<style>
  :root {
    --page: #e9e6e2;
    --clear: rgba(92, 88, 86, 0.55);
    --clear-layer: rgba(255, 255, 255, 0.10);
    --clear-edge: rgba(255, 255, 255, 0.55);
    --orange: #ee4d0a;
    --orange-soft: rgba(238, 77, 10, 0.82);
    --red: #d9252b;
    --ink: #2f2a28;
    --white: #ffffff;
    --silver: rgba(235, 235, 235, 0.9);
  }
  * { margin: 0; padding: 0; box-sizing: border-box; }
  html, body { width: 1200px; height: 800px; overflow: hidden; }
  body {
    background: var(--page);
    font-family: "Poppins", sans-serif;
    display: flex;
    align-items: center;
    justify-content: center;
    gap: 60px;
  }

  /* Clear card with cut corners */
  .card-wrap { filter: drop-shadow(0 10px 18px rgba(0,0,0,.2)); }
  .card {
    position: relative;
    width: 520px;
    height: 298px;
    background: var(--clear);
    clip-path: polygon(0 0, calc(100% - 34px) 0, 100% 34px, 100% 100%, 34px 100%, 0 calc(100% - 34px));
    overflow: hidden;
  }
  .card::before {            /* frosted inner layer */
    content: "";
    position: absolute;
    inset: 10px;
    background: var(--clear-layer);
    border: 1px solid var(--clear-edge);
    clip-path: polygon(0 0, calc(100% - 28px) 0, 100% 28px, 100% 100%, 28px 100%, 0 calc(100% - 28px));
  }
  .card::after {             /* gloss sheen */
    content: "";
    position: absolute;
    inset: 0;
    background: linear-gradient(125deg, rgba(255,255,255,.22) 0%, rgba(255,255,255,0) 45%);
    pointer-events: none;
  }

  .mark { display: flex; align-items: center; position: absolute; z-index: 1; }
  .mark-square { background: var(--orange-soft); flex: none; }
  .mark-name { line-height: 1.2; }

  /* Front */
  .front-mark { left: 44px; top: 88px; gap: 18px; }
  .front-mark .mark-square { width: 112px; height: 112px; }
  .front-mark .mark-name { font-weight: 600; font-size: 27px; color: var(--orange); width: 200px; }

  .front-signature { right: 40px; top: 58px; gap: 8px; }
  .front-signature .mark-square { width: 34px; height: 34px; }
  .front-signature .mark-name { font-size: 12px; color: var(--ink); width: 92px; }

  /* Back */
  .back-signature { left: 190px; top: 28px; gap: 8px; }
  .back-signature .mark-square { width: 40px; height: 40px; }
  .back-signature .mark-name { font-size: 12px; color: var(--ink); width: 92px; }

  .org-name {
    position: absolute; z-index: 1;
    left: 44px; top: 100px;
    font-weight: 600; font-size: 22px;
    color: var(--white);
  }
  .contact {
    position: absolute; z-index: 1;
    left: 110px; top: 142px;
    list-style: none;
    color: var(--white);
    font-size: 13px;
  }
  .contact li { display: flex; align-items: center; gap: 8px; margin-bottom: 10px; }
  .contact li.email { margin-left: -62px; }
  .contact .icon {
    width: 18px; height: 18px;
    background: var(--orange);
    display: flex; align-items: center; justify-content: center;
  }
  .wave { position: absolute; left: 0; bottom: 0; width: 520px; height: 298px; }
</style>
</head>
<body>

  <div class="card-wrap">
    <section class="card card-front" aria-label="Card front">
      <div class="mark front-mark">
        <span class="mark-square"></span>
        <span class="mark-name">Lanterns of Willow Creek</span>
      </div>
      <div class="mark front-signature">
        <span class="mark-square"></span>
        <span class="mark-name">Lanterns of Willow Creek</span>
      </div>
    </section>
  </div>

  <div class="card-wrap">
    <section class="card card-back" aria-label="Card back">
      <svg class="wave" viewBox="0 0 520 298" aria-hidden="true">
        <defs>
          <linearGradient id="waveFill" x1="0" y1="1" x2="1" y2="0">
            <stop offset="0" stop-color="#d9252b" stop-opacity=".9"/>
            <stop offset="1" stop-color="#ee4d0a" stop-opacity=".95"/>
          </linearGradient>
        </defs>
        <path d="M0 298 L0 272 C140 268 230 252 300 190 C360 138 430 92 520 86 L520 298 Z" fill="var(--silver)"/>
        <path d="M0 298 L0 282 C150 278 240 266 315 204 C375 154 440 110 520 104 L520 298 Z" fill="url(#waveFill)"/>
      </svg>

      <div class="mark back-signature">
        <span class="mark-square"></span>
        <span class="mark-name">Lanterns of Willow Creek</span>
      </div>

      <h1 class="org-name">Lanterns of Willow Creek</h1>

      <ul class="contact">
        <li>
          <span class="icon">
            <svg width="11" height="11" viewBox="0 0 24 24" aria-hidden="true"><path fill="#fff" d="M6.6 10.8a15.1 15.1 0 0 0 6.6 6.6l2.2-2.2a1 1 0 0 1 1-.25 11.4 11.4 0 0 0 3.6.57 1 1 0 0 1 1 1V20a1 1 0 0 1-1 1A17 17 0 0 1 3 4a1 1 0 0 1 1-1h3.5a1 1 0 0 1 1 1c0 1.25.2 2.45.57 3.57a1 1 0 0 1-.25 1z"/></svg>
          </span>
          555-014-7392
        </li>
        <li class="email">
          <span class="icon">
            <svg width="11" height="11" viewBox="0 0 24 24" aria-hidden="true"><path fill="#fff" d="M2 21 23 12 2 3v7l15 2-15 2z"/></svg>
          </span>
          email@lanternsofwillowcreek.org
        </li>
      </ul>
    </section>
  </div>

</body>
</html>
```